依頼詳細
このたびは、「緑茶ハイ・緑茶」専用メニュー表(A4片面)のデザインを募集いたします。

【メニュー表に入れていただきたい要素】
・ロゴ「凪色 Harbor」を、おしゃれなレトロ調で作成。メニュー表の上端にロゴを入れる。
・ユーモアで面白さもありつつ、少し高級感もあるデザイン。
・シリーズ化できる(これから緑茶以外にも紅茶ハイなども展開する可能性があります)
・「飲むならこの緑茶ハイがいいな!」と思われるようなデザインやキャッチコピー。
・飲食店の他メニュー表と一緒に置いていて、目を引くデザイン。

【コンペの流れ】
①ご応募ください。
②作成したデザインをご提出ください。
③コンペ終了後、採用者の選定をさせていただきます。

【デザイン提出方法】
PDFデータまたは、AIデータをお送りください。
※採用させていただいた場合、最終納品はイラストレーター形式(.ai)にてお願いします。

【備考】
ご提案いただいたデザインの編集依頼をすることがございます。
納期まで余裕をもってご提案頂けますと幸いです。
納期を過ぎてのご提案は受け付けておりませんので、予めご了承ください。
注意点】
コンペで採用となった場合、著作権は弊社に帰属します。

【継続依頼について】
スキル、センス、クオリティの高さなどにより、継続的な依頼を検討いたします。
記載項目
【メニュー表に入れていただきたい内容】
・緑茶ハイと緑茶の写真画像(デザイナー様の選定でお願いします)
・「緑茶ハイと緑茶」の値段が入れられる場所
(金額は仮で¥500と記載をお願いします)
・とっても美味しい静岡県産掛川市の茶葉を使用。
・無添加、無農薬のお茶粉。
・お茶粉のスティック写真を盛り込む(添付画像データをお使いください)。
※商品チラシデータを添付しています。
栄養や安全性、美味しさの詳細が書かれていますのでご覧ください。
サイズ
A4
ページ数
片面
希望イメージ
シンプル 複雑
単色 カラフル
暗い 明るい
日常 高級
遊び心 厳粛
未来的 伝統的
女性的 男性的
希望する色
緑系
納品ファイル
• イラストレーター形式 (.ai)
〆切を4/5に延長させていただきました!
どうか、デザイナーの方々のお力を貸してください!
よろしくお願いいたします。
みなさまのご協力をお待ちしております。
よろしくお願いいたします!
■ 選んだ理由

弊社のイメージするデザインに1番近かったため。

■ 提案者全員のお礼・コメント

素敵なデザインを作成していただき、ありがとうございます!

```html
<!DOCTYPE html>
<html lang="ja">
<head>
<meta charset="utf-8">
<title>凪色 Harbor 緑茶・緑茶ハイ メニュー</title>
<link rel="stylesheet" href="https://fonts.googleapis.com/css2?family=Shippori+Mincho+B1:wght@700;800&family=Cormorant+Garamond:wght@600;700&display=swap">
<style>
  :root{
    --bg-deep:#0f3a22;
    --bg-mid:#1c5331;
    --bg-light:#2b6a40;
    --cream:#f3f0dc;
    --gold:#c9a24a;
    --gold-light:#e4c77a;
    --tea-light:#c9dc7e;
    --tea-mid:#8fb342;
    --tea-dark:#5c8a2a;
    --badge:#2d6a3a;
  }
  *{margin:0;padding:0;box-sizing:border-box}
  html,body{width:846px;height:1200px;overflow:hidden;background:var(--bg-deep)}
  .menu{
    position:relative;width:846px;height:1200px;overflow:hidden;
    background:radial-gradient(ellipse at 50% 45%, var(--bg-light) 0%, var(--bg-mid) 45%, var(--bg-deep) 100%);
    font-family:"Shippori Mincho B1", serif;color:var(--cream);
  }
  .brush{position:absolute;inset:0}
  .photo{position:absolute;border-radius:10px 10px 18px 18px}
  .photo--greentea{left:550px;top:70px;width:250px;height:355px;
    background:linear-gradient(180deg,var(--tea-light) 0%,var(--tea-mid) 55%,var(--tea-dark) 100%)}
  .photo--highball{left:45px;top:690px;width:280px;height:470px;
    background:linear-gradient(180deg,var(--tea-light) 0%,var(--tea-mid) 60%,var(--tea-dark) 100%)}
  .tagline{position:absolute;top:55px;writing-mode:vertical-rl;font-size:44px;font-weight:800;
    letter-spacing:4px;color:var(--cream)}
  .tagline--1{left:158px}
  .tagline--2{left:218px}
  .item-en{position:absolute;font-family:"Cormorant Garamond", serif;font-weight:700;color:var(--gold-light);letter-spacing:1px}
  .item-ja{position:absolute;font-weight:800;color:var(--gold-light);line-height:1}
  .price{position:absolute;font-family:"Cormorant Garamond", serif;font-weight:700;color:var(--cream)}
  .greentea-en{left:300px;top:80px;font-size:34px}
  .greentea-ja{left:296px;top:130px;font-size:100px;letter-spacing:4px}
  .greentea-price{left:330px;top:238px;font-size:34px}
  .highball-en{left:340px;top:915px;font-size:32px}
  .highball-ja{left:345px;top:970px;font-size:104px;letter-spacing:2px}
  .highball-price{left:650px;top:1110px;font-size:42px}
  .brand{position:absolute;left:300px;top:430px;width:250px;text-align:center;color:var(--gold);font-weight:800}
  .brand__top,.brand__bottom{display:block;font-size:150px;line-height:1.05}
  .brand__en{display:block;font-family:"Shippori Mincho B1", serif;font-size:34px;letter-spacing:4px;margin:4px 0}
  .stick{position:absolute;left:170px;top:700px;width:26px;height:120px;transform:rotate(-12deg);
    background:linear-gradient(180deg,#e7d6a0,#c2412f 40%,#8f2a22);border-radius:3px}
  .badge{position:absolute;left:218px;top:688px;width:98px;height:98px;border-radius:50%;
    background:var(--badge);border:2px solid var(--gold-light);display:flex;flex-direction:column;
    align-items:center;justify-content:center;text-align:center;color:var(--cream);font-weight:700}
  .badge__note{font-size:9px;line-height:1.2;width:70px}
  .badge__main{font-size:15px;line-height:1.2;color:var(--gold-light);margin-top:3px}
</style>
</head>
<body>
<main class="menu">
  <svg class="brush" width="846" height="1200" role="img" aria-label="筆で描いた円と墨の流れ">
    <defs>
      <radialGradient id="ring" cx="50%" cy="50%" r="50%">
        <stop offset="70%" stop-color="#3a7a4c" stop-opacity="0"/>
        <stop offset="85%" stop-color="#3a7a4c" stop-opacity="0.35"/>
        <stop offset="100%" stop-color="#3a7a4c" stop-opacity="0"/>
      </radialGradient>
    </defs>
    <circle cx="470" cy="600" r="330" fill="url(#ring)"/>
    <ellipse cx="120" cy="80" rx="220" ry="70" fill="#3a7a4c" opacity="0.18"/>
    <ellipse cx="760" cy="1120" rx="220" ry="80" fill="#3a7a4c" opacity="0.18"/>
  </svg>

  <div class="photo photo--greentea" role="img" aria-label="氷入りの緑茶のグラス"></div>
  <div class="photo photo--highball" role="img" aria-label="氷入りの緑茶ハイのグラス"></div>

  <p class="tagline tagline--2">美味しい静岡県産</p>
  <p class="tagline tagline--1">掛川市産茶葉使用</p>

  <p class="item-en greentea-en">GreenTea</p>
  <h2 class="item-ja greentea-ja">緑茶</h2>
  <p class="price greentea-price">¥500</p>

  <h1 class="brand">
    <span class="brand__top">凪</span>
    <span class="brand__en">Harbor</span>
    <span class="brand__bottom">色</span>
  </h1>

  <div class="stick" role="img" aria-label="お茶粉のスティック"></div>
  <div class="badge">
    <span class="badge__note">お茶の葉をまるごと粉末に</span>
    <span class="badge__main">無添加<br>無農薬</span>
  </div>

  <p class="item-en highball-en">SHOCHU AND GREENTEA</p>
  <h2 class="item-ja highball-ja">緑茶ハイ</h2>
  <p class="price highball-price">¥500</p>
</main>
</body>
</html>
```